Talvoro Web Design

We need a redesign of our current website www.talvoro-example.com

THIS IS A DESIGN STAGE ONLY

We have attached details of the whole project for your understanding only

We do not want to change our Logo but do want to have a more modern and intuitive feel to the site.

The first stage is the design but we are also looking for a coder to take the site to the next level

Talvoro has a current website that has been in operation for the past 6 years the design was based around the Saas self-service model and while functional does not meet Talvoro needs with regard to the new positioning.

We are happy to stay in Fendrix or will look at alternatives

The purpose of the redesign is to align the look and feel of the website to meet our current new brand position and to provide a access point for the delivery of new content from Blogs and white papers as well as a portal for information for our current users for gathering Tips and Tricks and access to additional resources to assist them to provide feedback and get support.

Talvoro is Australia's only PPM (Project and Portfolio Management) software provider that caters to the needs of project managers and C-level executives looking for insights into the alignment of resources to business strategy and investment decisions.

As companies gain maturity in PPM there is a need for innovation and management of change beyond just implementation of tools this is why Talvoro has evolved from being a SaaS to becoming a SwS (Software with Service) provider.

Talvoro is recognized as the tool of choice amongst program and project managers that is able to provide the user with an intuitive reliable interface that is capable of evolving and maturing to meet and exceed client requirements.

We are able to provide people at the coalface with tools that enable them to manage resources, scope, time sheeting, issues, changes and risk with excellent reporting functionality.

For C-level executives we are able to provide Business Intelligence (BI) functionality and reporting by integrating the PPM data with other business management systems such as ERP and CRM to provide a insight beyond pure PPM reporting.

We are able to provide Project Management insights from years of experience working with our clients in developing solutions that are inline with the evolution that comes with change.

Please feel free to email me on nigel.brask@talvoro-example.com if you require any further details. A Site map and a wire frame is available.

Competitor sites include

www.plonverk-example.com
www.surmoza-example.com
www.qarnitel-example.com
www.velubra-example.com
Updates

Hi All 

We are getting some great designs coming in and really appreciate all of your efforts.

Some feedback to you all is that we have a preference for cleaner designs that take into account comprehension ability. So reverse type to us looks good but doesnt always get the cut through.

We have to remember that this is a marketing site first and foremost so what we are looking for is the ability to engage with our audience and get them to start to explore. That is upto us to provide great content and what we want from the design is the ability to be be able to engage with our Audience.

For your consideration please review this info from our marketing plan

There are 3 main communication groups inthe sales process.

Users-        These are the peoplewho will be at the coal face inputting the data and using the product on adaily basis. It is key to provide them with an easy to use and functional toolthat is able to provide them with the information they are looking for easily andintuitively. They have the capacity to say yes and can push the sale decisionup the chain. They equally have the power to say No and stop the sales processin its tracks. They will have a opinion who or what they feel is the best ofbreed and will try to influence the process.

Users are split into two groups.

Group1- They will be diploma if not degree qualifiedwill be a mix of Male and female with majority aged 18 to 35 they are at thecareer development stage of their life cycle normally on an income 45k to 70kper annum. We would position these people very strongly in the “What is in itfor me”.

Group2- PM who has used a variety of tools and systemsover the years they will be pre disposed to one or more systems and has morethan likely been exposed to MSP. Usually in the 30 to 50 year old age rangewith extensive on the job experience.

KeyInfluencers- These are the people who while notactually utilizing the software need to receive information in the form ofreports etc from the system. They normally don’t have the capacity to say yesbut they most certainly can say no. They will have come from a PM or IT roleand have a strong understanding of the PM processes. Influencers will be 30 to50 years of age they are at the family development stage with strong demandsfrom work and family predominantly male but not exclusively. They would bedegree qualified and possibly have completed or looking at additional studies. Therewill be an emphasis on getting the job done right. They are very time poor and hardto communicate with and engage. While being time poor they have an affinitywith and understand the greater good.

DecisionMakers- These are our key decision makers whilethey may not have direct input into the system or processes they are at the endof the day the people who approve the expenditure.

There is a huge demand for this person’stime with a multitude of people from internal employees and management,suppliers, customers, the community and potential suppliers. They are oftentravelling and going from one subject matter to another meeting after meeting.They will be at the stage where children are gaining some independents or leftthe home, career is stabilized and a clear path is formed. They are very directand deal in the facts and figures when it comes to decision making, they arenormally highly educated to the MBA or Doctorate level. They will be driven byoutcomes not the process of getting there.

 

A consistent theme across this group isthe following.

Psychographics

·Values time and considers ittheir single most limited resource.

·Excited about accepting andusing innovative ideas and products always wants to be at the fore front.

·Value adding has priority overprice

·Consistent web users: preferinternet over magazines and newspapers

Behavior

·They are leaders in productselection and respond to the opinions of the ‘Industry Experts’ when makingpurchase decisions.

·This group will look to theinternet to acquire the information

·Will make an informed decisionto purchase after due consideration.

·This group can be a powerfulsales force resulting from the referral network they build and use

Hope this helps

Hi All

Sorry for the delay we are in the final stages of decisions, so sorry we have had people away from the office who need to be involved in the process.

We will submit individual questions to those in the running and let all of the people who didnt get through this time as to why shortly.

We would like to thank you all for your efforts and submissions.

Regards

Nigel Brask 

Industry/Entity Type

Business Management

Requirements
Must have
• The scope of the website is to provide a modern functional website that is easy to navigate and provides a range of products and services to meet the needs of our potential clients and current users.

Two potential groups of viewers exist:
1. Potential Clients and users from the Project management community these would be split into 3 distinct groups. ( Please refer to Page 20 Talvoro marketing Plan)
a. Project Managers
b. Project Directors
c. Business Managers
2. Current Talvoro Users

The goal of website is to engage with the project management community reinforcing the Talvoro Brand as Software with Service the key ethos should be around the company being thought leaders and industry experts with a strong commitment to clients and the success of their Portfolio/Program Management Office

Maintaining a modern and user friendly site is of the highest importance in order to hold users attention and guide the viewer to information that will lead to a decision to pursue accreditation and association with the Talvoro Brand

We would like to guide potential clients to want to engage with us in assisting them to understand their current position in the K5R5 maturity model and to use us as a source for information and guidance.

Benefits for using the site should include:
• Information from a broad spectrum of Project Management professionals and recognized industry experts.
• Information on the Talvoro Product and Services
• Timely and up to date information that encourages readers to return to the site
• Call to action, and plans for potential users of Talvoro software.
• Demonstrate the benefits of accreditation and Call to action for current users to gain accreditation.
• Call to action for attending monthly webinars
• Ability to review past webinars, whitepapers etc.

```html
<!DOCTYPE html>
<html lang="en">
<head>
<meta charset="utf-8">
<title>Talvoro – Project Management Software</title>
<link rel="stylesheet" href="https://fonts.googleapis.com/css2?family=Roboto:wght@300;400;500;700;900&display=swap">
<style>
:root{
  --red:#ea3b24;
  --ink:#1a1a1a;
  --text:#555;
  --muted:#777;
  --btn:#6a6a6a;
  --line:#dcdcdc;
  --footer:#000;
  --footer-text:#8a8a8a;
  --footer-head:#b5b5b5;
}
*{margin:0;padding:0;box-sizing:border-box}
html,body{width:972px;height:1200px;overflow:hidden;background:#fff}
body{position:relative;font-family:"Roboto",Helvetica,Arial,sans-serif;color:var(--text);border-top:2px solid #111}
.abs{position:absolute}
a{color:inherit;text-decoration:none}

/* header */
.logo{left:154px;top:28px;display:flex;align-items:center;gap:5px;font-size:27px;font-weight:400;color:var(--ink);letter-spacing:-.5px}
.logo .dot{width:8px;height:8px;border-radius:50%;background:var(--red);margin-bottom:14px}
.main-nav{left:274px;top:40px;display:flex;align-items:center;font-size:10.5px;font-weight:500;color:#444;letter-spacing:.3px}
.main-nav a{padding:0 14px;border-right:1px solid #ccc;line-height:12px}
.main-nav a:first-child{padding-left:0}
.main-nav a.accent{color:var(--red)}
.main-nav .call{display:flex;align-items:center;gap:6px;padding-left:12px;font-size:9.5px;color:#888;font-weight:400}
.main-nav .call b{font-size:11px;color:var(--ink);font-weight:700}
.rule{left:0;width:972px;border-top:1px dotted #cfcfcf}

/* features */
.feature{top:110px;width:140px}
.feature svg{display:block;margin:0 0 10px 44px}
.feature h3{font-size:12px;font-weight:700;color:var(--ink);letter-spacing:-.3px;margin-bottom:6px}
.feature h3 span{color:var(--red)}
.feature p{font-size:8px;line-height:11px;color:var(--muted);margin-bottom:6px}
.btn-sm{display:inline-block;background:var(--btn);color:#fff;font-size:6.5px;padding:4px 5px;border-radius:2px;box-shadow:0 1px 0 #aaa}
.vsep{border-left:1px dotted #ccc}

/* hero */
.hero{left:0;top:248px;width:972px;height:268px;background:linear-gradient(#fff,#ececec)}
.hero-text{left:157px;top:343px;color:var(--ink)}
.hero-text .l1{font-size:18px;font-weight:500;line-height:20px}
.hero-text .l2{font-size:26px;font-weight:900;color:var(--red);letter-spacing:-1px;line-height:27px}
.hero-text .l3{font-size:26px;font-weight:900;letter-spacing:-1px;line-height:27px}
.btn-hero{left:155px;top:428px;width:140px;height:37px;background:#000;color:#fff;border-radius:3px;font-size:17px;font-weight:500;display:flex;align-items:center;justify-content:center;letter-spacing:-.5px}
.hero-photo{left:510px;top:258px;width:178px;height:258px;border-radius:80px 80px 0 0;background:linear-gradient(#f2ead9,#e7e2d8 60%,#dcdcdc)}

/* sub nav */
.sub-nav{left:0;top:516px;width:972px;height:28px;background:var(--red);box-shadow:0 4px 0 #cfcfcf;display:flex;align-items:center;padding-left:157px;font-size:8.5px;font-weight:500;color:#fff}
.sub-nav a{padding:0 16px;border-right:1px solid rgba(255,255,255,.7);line-height:10px}
.sub-nav a:first-child{padding-left:0}
.sub-nav a:last-child{border:none}

/* CTA */
.cta{top:583px}
.cta h4{font-size:11px;font-weight:700;color:var(--ink);letter-spacing:-.4px;margin-bottom:5px}
.cta h4 span{color:var(--red)}
.cta p{font-size:8px;line-height:11px;color:var(--muted)}
.btn-md{position:absolute;background:var(--btn);color:#fff;font-size:10px;font-weight:500;height:22px;display:flex;align-items:center;justify-content:center;border-radius:2px;box-shadow:0 1px 0 #aaa}
.date{left:581px;top:600px;width:27px;height:25px;background:#111;color:#fff;font-size:7px;line-height:8px;text-align:center;padding-top:3px;font-weight:700}
.date b{display:block;font-size:9px}
.webinar-line{left:621px;top:600px;font-size:8px;line-height:11px;color:var(--muted)}
.webinar-line b{color:#333}

/* blog */
.sec-title{font-size:13px;font-weight:700;color:var(--ink);letter-spacing:-.4px}
.sec-title span{color:var(--red)}
.thumb{border:2px solid #e2e2e2}
.post{width:305px}
.post h5{font-size:9.5px;font-weight:700;color:#333;margin-bottom:5px}
.post p{font-size:8.5px;line-height:12px;color:var(--text)}
.post .more{display:block;margin-top:5px;font-size:8px;color:var(--red)}
.mini{width:160px;font-size:8.3px;line-height:11.5px;color:var(--text)}
.mini b{display:block;color:#333;font-size:9px}

/* footer */
.footer{left:0;top:982px;width:972px;height:218px;background:var(--footer)}
.fcol{top:1003px;font-size:8px;color:var(--footer-text);line-height:12.7px}
.fcol h6{font-size:8.5px;font-weight:500;color:var(--footer-head);margin-bottom:11px}
.fsep{top:1000px;height:122px;border-left:1px dotted #333}
.copyright{left:155px;top:1163px;font-size:7.5px;color:#3d3d3d}
.social{left:460px;top:1166px;display:flex;gap:3px}
.social i{display:block;width:10px;height:10px;background:#666;border-radius:2px}
.flogo{left:712px;top:1152px;display:flex;align-items:center;gap:4px;font-size:24px;color:#555}
.flogo .dot{width:7px;height:7px;border-radius:50%;background:#555;margin-bottom:12px}
</style>
</head>
<body>

<!-- header -->
<div class="abs logo"><span>Talvoro</span><span class="dot"></span></div>
<nav class="abs main-nav">
  <a href="#">TOUR</a><a href="#">FEATURES</a><a href="#">PRICING</a>
  <a href="#" class="accent">LOGIN</a><a href="#" class="accent">SIGN UP</a>
  <span class="call">
    <svg width="11" height="11" viewBox="0 0 24 24"><path fill="#222" d="M6.6 10.8a15.1 15.1 0 0 0 6.6 6.6l2.2-2.2c.3-.3.7-.4 1-.2 1.1.4 2.3.6 3.6.6.6 0 1 .4 1 1V20c0 .6-.4 1-1 1C10.6 21 3 13.4 3 4c0-.6.4-1 1-1h3.5c.6 0 1 .4 1 1 0 1.3.2 2.5.6 3.6.1.3 0 .7-.2 1z"/></svg>
    Call Us Today: <b>(555) 014-2936</b>
  </span>
</nav>
<div class="abs rule" style="top:69px"></div>

<!-- features -->
<div class="abs feature" style="left:154px">
  <svg width="30" height="30" viewBox="0 0 30 30"><g fill="#ea3b24"><circle cx="15" cy="15" r="10"/><rect x="12" y="1" width="6" height="28" rx="1"/><rect x="1" y="12" width="28" height="6" rx="1"/><rect x="12" y="1" width="6" height="28" rx="1" transform="rotate(45 15 15)"/><rect x="12" y="1" width="6" height="28" rx="1" transform="rotate(-45 15 15)"/></g><circle cx="15" cy="15" r="4.5" fill="#fff"/></svg>
  <h3>Project <span>Management</span></h3>
  <p>Simple, easy to use project management software...</p>
  <a class="btn-sm" href="#">Read More</a>
</div>
<div class="abs vsep" style="left:288px;top:152px;height:55px"></div>
<div class="abs feature" style="left:304px">
  <svg width="30" height="30" viewBox="0 0 30 30" style="margin-left:50px"><path d="M6 2h13l6 6v20H6z" fill="none" stroke="#ea3b24" stroke-width="2.5"/><path d="M10 11h10M10 15h10M10 19h10M10 23h7" stroke="#ea3b24" stroke-width="2"/></svg>
  <h3>Time<span>sheets</span></h3>
  <p>Powerful hosted project time and status collection...</p>
  <a class="btn-sm" href="#">Read More</a>
</div>
<div class="abs vsep" style="left:458px;top:152px;height:55px"></div>
<div class="abs feature" style="left:476px">
  <svg width="30" height="30" viewBox="0 0 30 30" style="margin-left:48px"><path d="M15 2l12 6-12 6-12-6z" fill="#f26a4f"/><path d="M3 10l11 5.5V29L3 23z" fill="#ea3b24"/><path d="M27 10l-11 5.5V29l11-6z" fill="#c9301c"/></svg>
  <h3>Resource <span>Management</span></h3>
  <p>Plan, manage and control work for your whole organisation...</p>
  <a class="btn-sm" href="#">Read More</a>
</div>
<div class="abs vsep" style="left:637px;top:152px;height:55px"></div>
<div class="abs feature" style="left:655px">
  <svg width="34" height="30" viewBox="0 0 34 30" style="margin-left:50px"><path d="M17 1l16 28H1z" fill="#ea3b24"/><rect x="15.5" y="10" width="3" height="10" fill="#fff"/><rect x="15.5" y="22" width="3" height="3" fill="#fff"/></svg>
  <h3>Issues, Risks <span>and change</span></h3>
  <p>Track and report on issues, risk and change...</p>
  <a class="btn-sm" href="#">Read More</a>
</div>
<div class="abs rule" style="top:246px"></div>

<!-- hero -->
<div class="abs hero"></div>
<div class="abs hero-text">
  <div class="l1">SIMPLE, EASY TO USE</div>
  <div class="l2">PROJECT MANAGEMENT</div>
  <div class="l3">SOFTWARE</div>
</div>
<a class="abs btn-hero" href="#">READ MORE</a>
<div class="abs hero-photo" role="img" aria-label="Photo of a businesswoman in a light suit holding a tablet"></div>

<nav class="abs sub-nav">
  <a href="#">Products &amp; Services</a><a href="#">About Us</a><a href="#">News &amp; Events</a>
  <a href="#">K5R5 Self Testing</a><a href="#">Blog</a><a href="#">Accreditation</a>
  <a href="#">Our Uniqueness</a><a href="#">Contact Us</a>
</nav>

<!-- calls to action -->
<div class="abs cta" style="left:154px;width:190px">
  <h4>SEE IT IN <span>ACTION</span></h4>
  <p>Login and see the power of Talvoro for yourself in our demo enviorment...</p>
</div>
<a class="btn-md" href="#" style="left:154px;top:632px;width:83px">LOGIN HERE</a>
<div class="abs vsep" style="left:346px;top:580px;height:80px"></div>
<div class="abs cta" style="left:362px;width:190px">
  <h4>JOIN THIS MONTH'S <span>WEBINAR</span></h4>
  <p>Duis autem vel eum iriure dolor in hendrerit in vulputate velit esse...</p>
</div>
<a class="btn-md" href="#" style="left:361px;top:631px;width:102px">REGISTER HERE</a>
<div class="abs vsep" style="left:561px;top:580px;height:80px"></div>
<div class="abs cta" style="left:581px;top:580px">
  <h4>REVIEW PAST <span>WEBINARS, WHITEPAPERS</span></h4>
</div>
<div class="abs date"><b>16</b>JULY</div>
<div class="abs webinar-line"><b>Duis autem vel eum iriure dolor</b>Hendrerit in vulputate velit esse...</div>
<a class="btn-md" href="#" style="left:619px;top:632px;width:83px">VIEW MORE</a>
<div class="abs rule" style="top:704px"></div>

<!-- blog -->
<h2 class="abs sec-title" style="left:154px;top:726px">Our Lastest <span>Blog Posts</span></h2>
<div class="abs thumb" style="left:154px;top:759px;width:69px;height:65px;background:linear-gradient(#f4f4f4,#d8d2cc)" role="img" aria-label="Portrait photo of a businesswoman"></div>
<div class="abs post" style="left:233px;top:762px">
  <h5>Lorem ipsum dolor sit amet, consectetuer adipiscing elit,</h5>
  <p>Sed diam nonummy nibh euismod tincidunt ut laoreet dolore magna aliquam erat volutpat. Ut wisi enim ad minim veniam, quis nostrud exerci tation ullamcorper suscipit lobortis nisl ut aliquip ex ea commodo consequat&nbsp; [...]</p>
  <a class="more" href="#">Read more »</a>
</div>
<div class="abs" style="left:233px;top:852px;width:294px;border-top:1px dotted #ccc"></div>
<div class="abs thumb" style="left:154px;top:871px;width:69px;height:65px;background:linear-gradient(#f6f6f6,#d9d3cd)" role="img" aria-label="Portrait photo of a smiling businessman"></div>
<div class="abs post" style="left:233px;top:875px">
  <h5>Lorem ipsum dolor sit amet, consectetuer adipiscing elit,</h5>
  <p>Duis autem vel eum iriure dolor in hendrerit in vulputate velit esse molestie consequat, vel illum dolore eu feugiat nulla facilisis at vero eros et accumsan et iusto odio dignissim qui blandit praesent luptatum zzril delenit augue duis dolore te feugait nulla facilisi&nbsp; [...]</p>
  <a class="more" href="#">Read more »</a>
</div>
<div class="abs vsep" style="left:561px;top:728px;height:230px"></div>

<h2 class="abs sec-title" style="left:581px;top:726px">From The <span>Blog</span></h2>
<div class="abs thumb" style="left:583px;top:759px;width:47px;height:46px;background:linear-gradient(#6b6b6b,#2a2a2a)" role="img" aria-label="Photo of a man in a suit"></div>
<div class="abs mini" style="left:643px;top:762px"><b>Lorem ipsum dolor sit amet,</b>consectetuer adipiscing elit, Sed diam nonummy nibh euismod [...]</div>
<div class="abs" style="left:581px;top:820px;width:222px;border-top:1px dotted #ccc"></div>
<div class="abs thumb" style="left:583px;top:836px;width:47px;height:46px;background:linear-gradient(#d0d0d0,#8e8e8e)" role="img" aria-label="Black and white photo of a smiling woman"></div>
<div class="abs mini" style="left:643px;top:839px"><b>Lorem ipsum dolor sit amet,</b>consectetuer adipiscing elit, Sed diam nonummy nibh euismod [...]</div>
<div class="abs" style="left:581px;top:897px;width:222px;border-top:1px dotted #ccc"></div>
<div class="abs thumb" style="left:583px;top:913px;width:47px;height:46px;background:linear-gradient(135deg,#e8ecef,#8a6a52)" role="img" aria-label="Photo of a woman at a desk"></div>
<div class="abs mini" style="left:643px;top:916px"><b>Lorem ipsum dolor sit amet,</b>consectetuer adipiscing elit, Sed diam nonummy nibh euismod [...]</div>

<!-- footer -->
<footer class="abs footer"></footer>
<div class="abs fcol" style="left:155px"><h6>Products &amp; Services</h6>Talvoro Software<br>Talvoro Support<br>PMS<br>K5R5 Testing</div>
<div class="abs fsep" style="left:247px"></div>
<div class="abs fcol" style="left:264px"><h6>About Us</h6>The Company<br>Why Talvoro<br>Mission &amp; Vision<br>Our People<br>Our Clients<br>Our Partners</div>
<div class="abs fsep" style="left:345px"></div>
<div class="abs fcol" style="left:358px"><h6>News &amp; Events</h6>Webinars<br>Newsletters<br>Release Information<br>Road Map<br>Release Timing</div>
<div class="abs fsep" style="left:455px"></div>
<div class="abs fcol" style="left:466px"><h6>K5R5 Self Testing</h6>K5R5 Modeling<br>K5R5 Scenario<br>Register For Test</div>
<div class="abs fsep" style="left:558px"></div>
<div class="abs fcol" style="left:570px"><h6>Blog</h6>PMO TODAY<br>Thoughts of a PM<br>What Makes a Great PMO</div>
<div class="abs fsep" style="left:679px"></div>
<div class="abs fcol" style="left:691px"><h6>Accreditation</h6>Benefits of Accreditation<br>How To Get Accredited<br>Register<br>Accredited Users Area<br>Forum<br>White Papers<br>Research<br>Advanced Help User Guide</div>
<div class="abs" style="left:155px;top:1142px;width:650px;border-top:1px solid #222"></div>
<div class="abs copyright">© 2003 - 2012 talvoro pty. ltd. All Rights Reserved</div>
<div class="abs social"><i></i><i></i><i></i><i></i><i></i></div>
<div class="abs flogo"><span>Talvoro</span><span class="dot"></span></div>

</body>
</html>
```